one page flyer for Harborline Commerce Summit 2015

We need a 1-page flyer design for a government-sponsored event based in San Francisco called Harborline Commerce Summit 2015.

Please see attached invite for content for flyer. I will add an agenda similar to Qorv TX in the draft.

Please reserve space for key content:
- Date: October 4, 2015, 9am - 1pm
- Entertainment featuring Vietnam's leading artists and performers
- Event sponsors: Corvel Bureau of Commerce and Vietnam, Lindquay Exchange Desk in San Francisco & Orvane Delegation Hall in San Francisco

Please create the template that allows me to enter copy.

Target Market(s)

Business Professionals

Industry/Entity Type

Business

Font styles to use
Serif
Script

Requirements
Must have
• Logo, Event date, sponsors, photos
• Easy to read
Nice to have
• Flags of US and Vietnam
• Links to logo: www. Crvb.gov.zq; www.orvanedelegation-hq.org/en/
Should not have
• this is a serious government-sponsored event so don't need flowery graphics.

```html
<!DOCTYPE html>
<html lang="en">
<head>
<meta charset="utf-8">
<title>Harborline Commerce Summit 2015</title>
<link href="https://fonts.googleapis.com/css2?family=Playfair+Display:wght@400;700&family=Great+Vibes&family=Oswald:wght@500;600&family=Open+Sans:wght@400;600&display=swap" rel="stylesheet">
<style>
  :root {
    --red: #b5191f;
    --red-deep: #8e1015;
    --gold: #f5c518;
    --ink: #333333;
    --muted: #555555;
    --paper: #ffffff;
  }
  * { margin: 0; padding: 0; box-sizing: border-box; }
  html, body { width: 849px; height: 1200px; overflow: hidden; background: var(--paper); }
  .flyer {
    position: relative; width: 849px; height: 1200px; overflow: hidden;
    font-family: "Open Sans", Arial, sans-serif; color: var(--ink); background: var(--paper);
  }
  .backdrop { position: absolute; inset: 0; }
  .header-org {
    position: absolute; top: 28px; width: 250px;
    font-size: 14px; line-height: 1.4;
    color: var(--paper); text-transform: uppercase; letter-spacing: 0.5px;
  }
  .header-org.left { left: 40px; }
  .header-org.right { right: 40px; width: 230px; }
  .header-badge {
    position: absolute; left: 364px; top: 8px; width: 120px; height: 120px;
    border-radius: 50%; background: var(--red); border: 5px solid var(--gold);
  }
  .invite {
    position: absolute; top: 198px; left: 0; width: 100%; text-align: center;
    font-size: 16px; line-height: 1.45; color: var(--muted);
  }
  .invite .event-name { color: var(--red); font-weight: 600; }
  .flag { position: absolute; top: 282px; width: 118px; height: 118px; border-radius: 50%;
    box-shadow: 0 4px 10px rgba(0,0,0,0.35); overflow: hidden; }
  .flag.us { left: 52px; }
  .flag.vn { left: 679px; }
  .anniversary {
    position: absolute; top: 300px; left: 190px; width: 469px; text-align: center;
  }
  .anniversary .title {
    font-family: "Playfair Display", Georgia, serif; font-weight: 400;
    font-size: 40px; line-height: 1; color: var(--red); letter-spacing: 0.5px;
  }
  .anniversary .subtitle {
    font-family: "Oswald", Arial, sans-serif; font-weight: 500;
    font-size: 22px; line-height: 1; margin-top: 8px; color: var(--ink); letter-spacing: 0.3px;
  }
  .years-ribbon { position: absolute; top: 384px; left: 319px; width: 210px; height: 34px; }
  .years-ribbon span {
    position: absolute; inset: 0; display: flex; align-items: center; justify-content: center;
    font-family: "Oswald", Arial, sans-serif; font-weight: 500; font-size: 19px; color: var(--paper); letter-spacing: 1px;
  }
  .date-label {
    position: absolute; top: 428px; left: 0; width: 100%; text-align: center;
    font-family: "Great Vibes", cursive; font-size: 42px; color: var(--ink); line-height: 1;
  }
  .date-value {
    position: absolute; top: 470px; left: 0; width: 100%; text-align: center;
    font-family: "Playfair Display", Georgia, serif; font-size: 62px; color: var(--red); line-height: 1;
  }
  .time-pill {
    position: absolute; top: 556px; left: 359px; width: 130px; height: 32px; border-radius: 16px;
    background: var(--red); color: var(--paper); text-align: center;
    font-family: "Oswald", Arial, sans-serif; font-weight: 500; font-size: 18px; line-height: 32px;
  }
  .feature-banner { position: absolute; top: 622px; left: 50px; width: 749px; height: 96px; }
  .feature-banner p {
    position: absolute; inset: 0; display: flex; align-items: center; justify-content: center;
    text-align: center; font-family: "Oswald", Arial, sans-serif; font-weight: 600;
    font-size: 28px; line-height: 1.2; color: var(--gold); text-transform: uppercase; letter-spacing: 0.5px;
  }
  .sponsors { position: absolute; top: 758px; left: 160px; width: 620px; }
  .sponsors h2 {
    font-family: "Playfair Display", Georgia, serif; font-weight: 700; font-size: 24px; color: var(--red);
    margin-bottom: 10px;
  }
  .sponsors ul { list-style: none; }
  .sponsors li {
    position: relative; padding-left: 30px; font-size: 19px; line-height: 33px; color: var(--ink);
  }
  .sponsors li::before {
    content: ""; position: absolute; left: 0; top: 10px; width: 13px; height: 13px;
    border-radius: 50%; background: var(--red);
  }
  .parking {
    position: absolute; top: 1100px; left: 0; width: 100%; text-align: center;
    color: var(--paper); font-size: 14px; line-height: 1.6;
  }
  .parking strong { font-weight: 600; }
</style>
</head>
<body>
<main class="flyer">
  <svg class="backdrop" width="849" height="1200" viewBox="0 0 849 1200" aria-hidden="true">
    <path d="M0 0 H849 V150 Q424 60 0 150 Z" fill="var(--red)"/>
    <path d="M0 152 Q424 62 849 152" fill="none" stroke="var(--gold)" stroke-width="6"/>
    <path d="M0 1080 Q424 1020 849 1080 V1200 H0 Z" fill="var(--red)"/>
    <path d="M0 1074 Q424 1014 849 1074" fill="none" stroke="var(--gold)" stroke-width="6"/>
  </svg>

  <p class="header-org left">Corvel Bureau<br>of Commerce</p>
  <div class="header-badge" aria-hidden="true"></div>
  <p class="header-org right">Orvane Delegation Hall<br>in San Francisco</p>

  <p class="invite">On the occasion of 20th anniversary of the establishment of<br>Vietnam – U.S. diplomatic relations<br>We would like to cordially invite you to attend <span class="event-name">Harborline Commerce Summit 2015</span></p>

  <svg class="flag us" viewBox="0 0 140 140" aria-label="United States flag">
    <rect width="140" height="140" fill="#ffffff"/>
    <g fill="#c8102e">
      <rect y="0" width="140" height="11"/><rect y="22" width="140" height="11"/>
      <rect y="44" width="140" height="11"/><rect y="66" width="140" height="11"/>
      <rect y="88" width="140" height="11"/><rect y="110" width="140" height="11"/>
      <rect y="132" width="140" height="11"/>
    </g>
    <rect width="70" height="77" fill="#1f3a7a"/>
  </svg>
  <svg class="flag vn" viewBox="0 0 140 140" aria-label="Vietnam flag">
    <rect width="140" height="140" fill="#da251d"/>
    <polygon points="70,32 79,60 108,60 85,77 93,105 70,88 47,105 55,77 32,60 61,60" fill="#ffde00"/>
  </svg>

  <div class="anniversary">
    <h1 class="title">20TH ANNIVERSARY</h1>
    <p class="subtitle">VIETNAM - U.S. DIPLOMATIC RELATIONS</p>
  </div>
  <div class="years-ribbon">
    <svg width="210" height="34" viewBox="0 0 210 34" aria-hidden="true">
      <polygon points="0,0 210,0 199,17 210,34 0,34 11,17" fill="var(--red)"/>
    </svg>
    <span>1995 - 2015</span>
  </div>

  <p class="date-label">Date</p>
  <p class="date-value">October 4, 2015</p>
  <p class="time-pill">9am - 1pm</p>

  <div class="feature-banner">
    <svg width="749" height="96" viewBox="0 0 749 96" aria-hidden="true">
      <polygon points="0,0 749,0 729,48 749,96 0,96 20,48" fill="var(--red)"/>
    </svg>
    <p>Entertainment featuring Vietnam's<br>leading artists and performers</p>
  </div>

  <section class="sponsors">
    <h2>Event sponsors :</h2>
    <ul>
      <li>Vietnam's Trade and Investment Policy</li>
      <li>Orvane Delegation Hall in San Francisco</li>
      <li>Lindquay Exchange Desk in San Francisco</li>
      <li>Opportunities to do business in Vietnam</li>
      <li>Business matching with Vietnamese business delegation</li>
      <li>Product display, music performance and more</li>
    </ul>
  </section>

  <div class="parking">
    <p><strong>Parking Available</strong> at Tidewell Garage, 418 Marlow St, San Francisco, CA 94108</p>
    <p>Brenlow Annex Building 512 Calden St., San Francisco, CA 94108</p>
    <p><strong>9:00am - 1:00pm</strong></p>
  </div>
</main>
</body>
</html>
```